Atelier Greta Voss Coming Soon

Launching a online mid century furniture business. I'm participating in an antiques fair prior to the website launch. I'd like a 1 page flyer that highlights a sampling of some iconic pieces and invites people to check out the website soon. If possible, I'd also like a Word template for a tear sheet (a one page doc that has the company logo and contact info, a picture of the item, a field for description and dimensions). The following is an example of a tear sheet...http://www.kbtcabinetworks.example/uploads/4/8/1/3/4813902/vesper_oak_low_side_chair.pdf. I'd prefer a smaller slot for the image (maybe one side of the page) and a much larger area for description and dimensions (as its vintage furniture I'll need to report on condition).

I've attached a few sample pieces of furniture, the company logo, contact information, and a room that included furniture from the business. The color palette for the business is orange, black, white and gray.

Target Market(s)

Potential Customers.....

Industry/Entity Type

Retail

Font styles to use
Other font styles liked:
• I think the fonts should be similar to the ones used in the logo and the business card (see attached)

Colors
f37122
1b1b1b
ebebeb

Requirements
Must have
• An elegant clean look and feel (although its a mid century furniture business I don't carry kitschy items...just really beautiful classic high-end pieces). It should highlight the beauty of the furniture and provide contact information.

```html
<!DOCTYPE html>
<html lang="en">
<head>
<meta charset="utf-8">
<title>Atelier Greta Voss — Flyer</title>
<link href="https://fonts.googleapis.com/css2?family=Antonio:wght@100;300&family=Open+Sans:wght@400&display=swap" rel="stylesheet">
<style>
  :root {
    --orange: #f37122;
    --ink: #1b1b1b;
    --paper: #ebebeb;
    --backdrop: #e07a3c;
    --photo-glow: #f0c89a;
    --photo-light: #d9a273;
    --photo-mid: #9a6a44;
    --photo-brick: #6e4a36;
    --photo-dark: #2e1e14;
  }
  * { margin: 0; padding: 0; box-sizing: border-box; }
  html, body {
    width: 1200px; height: 1200px; overflow: hidden;
    background: var(--backdrop);
  }
  .flyer {
    position: absolute;
    left: 220px; top: 108px;
    width: 760px; height: 984px;
    background: var(--paper);
  }
  .hero-photo {
    position: absolute;
    left: 34px; top: 34px;
    width: 692px; height: 690px;
    background:
      radial-gradient(ellipse 34% 30% at 80% 72%, rgba(240,200,154,0.85) 0%, rgba(240,200,154,0) 100%),
      radial-gradient(ellipse 30% 24% at 30% 78%, rgba(217,162,115,0.7) 0%, rgba(217,162,115,0) 100%),
      radial-gradient(ellipse 45% 30% at 55% 30%, rgba(240,200,154,0.75) 0%, rgba(240,200,154,0) 100%),
      linear-gradient(180deg, var(--photo-light) 0%, var(--photo-mid) 35%, var(--photo-dark) 52%, var(--photo-brick) 64%, var(--photo-mid) 100%);
  }
  .hero-frame {
    position: absolute;
    left: 22px; top: 22px; right: 22px; bottom: 22px;
    border: 2px solid rgba(255,255,255,0.85);
  }
  .hero-wordmark {
    position: absolute;
    left: 44px; top: 40px;
    font-family: 'Antonio', sans-serif;
    font-weight: 100;
    font-size: 66px;
    letter-spacing: 4px;
    color: rgba(255,255,255,0.8);
    text-transform: uppercase;
    white-space: nowrap;
  }
  .brand-name {
    position: absolute;
    left: 40px; top: 736px;
    font-family: 'Antonio', sans-serif;
    font-weight: 300;
    font-size: 80px;
    letter-spacing: 3px;
    line-height: 1;
    color: var(--ink);
    text-transform: uppercase;
    white-space: nowrap;
  }
  .brand-mark {
    display: inline-block;
    width: 18px; height: 18px;
    background: var(--orange);
    margin-right: 16px;
    vertical-align: middle;
    position: relative; top: -6px;
  }
  .contact {
    position: absolute;
    left: 48px; top: 850px;
    font-family: 'Open Sans', sans-serif;
    font-size: 17px;
    line-height: 1.35;
    color: var(--ink);
    list-style: none;
  }
  .contact .divider { color: var(--orange); margin: 0 4px; }
  .accent-rule {
    position: absolute;
    right: 40px; top: 856px;
  }
</style>
</head>
<body>
  <main class="flyer">
    <div class="hero-photo" role="img" aria-label="Styled living room with a dark cabinet, ring-back armchairs, a gilded chest with carved panels before a brick wall and a cream lounge chair, in warm sepia tones">
      <div class="hero-frame"></div>
      <p class="hero-wordmark">Atelier Greta Voss</p>
    </div>

    <h1 class="brand-name"><span class="brand-mark"></span>Atelier Greta Voss</h1>

    <svg class="accent-rule" width="40" height="16" viewBox="0 0 40 16" aria-hidden="true">
      <g stroke="#f37122" stroke-width="2">
        <line x1="0" y1="5" x2="16" y2="5"/><line x1="0" y1="11" x2="16" y2="11"/>
        <line x1="24" y1="5" x2="40" y2="5"/><line x1="24" y1="11" x2="40" y2="11"/>
      </g>
    </svg>

    <ul class="contact">
      <li>Renata Kolar</li>
      <li>Office <span class="divider">||</span>555-014-2090</li>
      <li>Mobile <span class="divider">||</span>555-017-5176</li>
      <li>renata@ateliergretavoss.example</li>
      <li>www.ateliergretavoss.example</li>
    </ul>
  </main>
</body>
</html>
```